Header/Logo Redesign

****WE HAVE FOUND THE DESIGNER WHO WILL BE HANDLING THIS PROJECT. PLEASE DONT SUBMIT ANY MORE DESIGNS.****
We have been working with a Web/Logo Designer on a new header and logo for our site. We like some of it, but other things need changing.
Overall Look: We are looking for something that is professional, yet still fresh. Most business two business websites seem old fashinoned. The site we like most is www.ledgerkite.com.
Header Thoughts:
-We like the color at the top of the header. The light purple on the menu bar is a little dull though. It seems to be grayed out too much. Notice the pop that www.ledgerkite.com has. We need that pop.
-The fonts on the menu bar don't pop either. I don't know if it is because the font is bad or the thickness of the font is bad or what.
-We are not sold on the green color in the logo and header. It is pretty good, but maybe we can test other colors?
Logo Thoughts:
-I am not sold on the green color. It is pretty good, but maybe test it out with some other colors?
-The logo does not pop like the www.ledgerkite.com logo pops.
-We had started thinking about doing an owl as part of our name/logo or maybe some other type of animal. Look at the ideas I had sent our original graphic designer.
A. http://markgrove.com/gallery/detail/113160 - i like that is simple, a little abstract, but I don't like that it is sort of evil.
B. http://markgrove.com/gallery/detail/61169 - i like that is abstract.
C. http://pixelbrine.files.hostplank.com/2012/05/tabrisk1.jpg - i like the slightly abstract.
D. http://snapquill.com/shots/353825-O-W-L - good - abrstract and slightly turned.
Target Market(s)
Sales and Marketing People - primarily a masculine audience in their 20s to 40s.
Industry/Entity Type
Business
Look and feel

```html
<!DOCTYPE html>
<html lang="en">
<head>
<meta charset="utf-8">
<title>Scoutline Header</title>
<link rel="stylesheet" href="https://fonts.googleapis.com/css2?family=Lato:wght@400;700;900&display=swap">
<style>
  :root {
    --night: #2a0f47;
    --menu: #7b52a3;
    --white: #ffffff;
    --orange-top: #f89a2a;
    --orange-bottom: #f0661e;
    --sky: #1ab2e8;
    --sky-deep: #0a94cc;
    --field: #d7d7d7;
    --field-text: #666666;
    --tab-text: #4a4a4a;
    --search-field: #fbf1f2;
  }
  * { box-sizing: border-box; margin: 0; padding: 0; }
  html, body { width: 1200px; height: 202px; overflow: hidden; background: var(--white); }
  body { position: relative; font-family: "Lato", sans-serif; }

  .topbar { position: absolute; left: 0; top: 0; width: 1200px; height: 88px; background: var(--night); }
  .menubar { position: absolute; left: 0; top: 88px; width: 1200px; height: 36px; background: var(--menu); }

  .brand { position: absolute; left: 112px; top: 28px; height: 30px; display: flex; align-items: center; gap: 8px; }
  .brand-dot { width: 18px; height: 18px; border-radius: 50%; background: var(--white); }
  .brand-name { font-weight: 900; font-size: 32px; color: var(--white); line-height: 1; letter-spacing: 0.2px; }

  .btn {
    position: absolute; display: flex; align-items: center; justify-content: center;
    background: linear-gradient(var(--orange-top), var(--orange-bottom));
    color: var(--white); font-weight: 700; border-radius: 3px;
  }
  .btn-new { left: 117px; top: 95px; width: 60px; height: 21px; font-size: 13px; }
  .nav-link { position: absolute; top: 98px; color: var(--white); font-weight: 700; font-size: 13px; transform: translateX(-50%); }
  .nav-people { left: 226px; }
  .nav-companies { left: 326px; }
  .nav-downloads { left: 439px; }

  .search-label { position: absolute; left: 783px; top: 98px; color: var(--white); font-weight: 700; font-size: 13px; }
  .search-field { position: absolute; left: 841px; top: 96px; width: 173px; height: 20px; background: var(--search-field); }
  .btn-go { left: 1028px; top: 96px; width: 59px; height: 20px; font-size: 13px; }

  .login-panel { position: absolute; left: 497px; top: 0; width: 268px; height: 158px; background: linear-gradient(var(--sky-deep), var(--sky) 40%, #22bcef); }
  .tab { position: absolute; top: 0; height: 30px; display: flex; align-items: center; justify-content: center; font-weight: 700; font-size: 12px; }
  .tab-login { left: 7px; width: 120px; background: var(--white); color: var(--tab-text); }
  .tab-signup { left: 127px; width: 127px; background: var(--sky-deep); color: var(--white); }
  .login-box { position: absolute; left: 14px; top: 30px; width: 240px; height: 114px; background: var(--white); box-shadow: 1px 2px 3px rgba(0,0,0,0.25); }
  .field { position: absolute; left: 11px; width: 218px; height: 23px; background: var(--field); color: var(--field-text); font-size: 11px; padding-left: 9px; display: flex; align-items: center; }
  .field-user { top: 11px; }
  .field-pass { top: 45px; }
  .btn-login { left: 173px; top: 77px; width: 56px; height: 28px; font-size: 12px; border-radius: 6px 2px 2px 6px; }
</style>
</head>
<body>
  <header>
    <div class="topbar"></div>
    <nav class="menubar"></nav>

    <div class="brand"><span class="brand-dot"></span><span class="brand-name">Scoutline</span></div>

    <span class="btn btn-new">New</span>
    <span class="nav-link nav-people">People</span>
    <span class="nav-link nav-companies">Companies</span>
    <span class="nav-link nav-downloads">Downloads</span>

    <span class="search-label">Search</span>
    <div class="search-field"></div>
    <span class="btn btn-go">Go</span>

    <div class="login-panel">
      <div class="tab tab-login">Account Login</div>
      <div class="tab tab-signup">Free Signup</div>
      <div class="login-box">
        <div class="field field-user">username</div>
        <div class="field field-pass">password</div>
        <span class="btn btn-login">Login</span>
      </div>
    </div>
  </header>
</body>
</html>
```